Corporate Design für Projektmanagement Firma
Vielen Dank für die Erarbeitung des Gewinnerdesigns. Auf Anfragen zur Anpassung von Designvorschlägen wurde prompt und mit ausgezeichneten Arbeitsergebnissen reagiert. Interessanterweise war gleich das erste Design das Gewinnerdesign - es wurde also auf Grundlage meiner Projektbeschreibung gleich das richtige Format getroffen. Hut ab! Danke auch für die unkomplizierte Übergabe der Dateien. Ich kann R olek auf jeden Fall weiterempfehlen.
Zielgruppe
Die Firma erbringt Projektmanagement- und Projektsteuerungsleistungen in der Baubranche für öffentliche Auftraggeber (größerer Anteil) und private Bauherren (kleinerer Anteil). Sie bietet außerdem strategische Organisationsberatung an, wenn es darum geht ein Projekt von Beginn an optimal aufzusetzen. Agiles Projektmanagement (in der Baubranche) ist ein Thema welches wir gern entwickeln wollen.
Aufgabenstellung
Die zu repräsentierende Firma lautet "Marlox Projektmanagement GmbH". Das Logo könnte die Initialen MaPM enthalten, gern mit kleinem e, oder auch nur kleine Buchstaben. Im Briefkopf und auf der Visitenkarte sollte der Firmenname ausgeschrieben auftauchen (ggf. in Kombi mit einem Logo?).
Eine mögliche Idee wäre die Verwendung eines Dreiecks als Symbol der Projektsteuerung- quasi das goldene Dreieck der Projektsteuerung (Kosten, Termine, Qualitäten). Das Design sollte eher schlicht, edel und geradlinig sein, nicht verspielt.

```html
<!DOCTYPE html>
<html lang="de">
<head>
<meta charset="utf-8">
<title>Marlox Projektmanagement – Geschäftsausstattung</title>
<link rel="stylesheet" href="https://fonts.googleapis.com/css2?family=Open+Sans:wght@300;400;600;700&display=swap">
<style>
  :root {
    --brand-blue: #0b4c8e;
    --brand-grey: #58585a;
    --text-dark: #3a3a3a;
    --paper: #ffffff;
    --backdrop: #d9d9d7;
    --rule: #9a9a9a;
  }
  * { box-sizing: border-box; margin: 0; padding: 0; }
  html, body { width: 1200px; height: 1198px; overflow: hidden; }
  body {
    position: relative;
    background: var(--backdrop);
    font-family: "Open Sans", Arial, sans-serif;
    color: var(--text-dark);
  }

  /* Wordmark */
  .wordmark { position: absolute; display: flex; align-items: center; gap: 10px; }
  .wordmark .dot { border-radius: 50%; flex: none; }
  .wordmark .name { font-weight: 700; line-height: 1; letter-spacing: 0.02em; }
  .wordmark .descriptor { font-weight: 700; line-height: 1; letter-spacing: 0.06em; display: block; margin-top: 4px; }

  /* Letterhead */
  .letterhead {
    position: absolute; left: 72px; top: 84px; width: 719px; height: 1016px;
    background: var(--paper);
  }
  .letterhead .wordmark { left: 108px; top: 66px; color: var(--brand-blue); }
  .letterhead .wordmark .dot { width: 38px; height: 38px; background: var(--brand-blue); }
  .letterhead .wordmark .name { font-size: 32px; }
  .letterhead .wordmark .descriptor { font-size: 11px; }
  .letter-rule { position: absolute; left: 168px; top: 298px; width: 1px; height: 446px; background: var(--rule); }
  .letter-body {
    position: absolute; left: 190px; top: 420px; width: 480px;
    font-size: 10.6px; line-height: 14.4px;
  }
  .letter-body p { margin-bottom: 14.4px; }
  .letter-body .closing { margin-top: 43px; }
  .letter-body .signature { margin-top: 15px; }
  .contact-icon { position: absolute; left: 154px; top: 798px; }
  .sender {
    position: absolute; right: 549px; top: 836px; text-align: right;
    font-size: 10.2px; line-height: 13.2px;
  }
  .sender strong { font-weight: 700; }
  .sender .group { margin-bottom: 13px; }
  .letter-band { position: absolute; left: 0; bottom: 0; width: 100%; height: 24px; background: var(--brand-blue); }

  /* Stand-alone wordmark */
  .wordmark.standalone { left: 836px; top: 88px; color: var(--brand-grey); }
  .standalone .dot { width: 62px; height: 62px; background: var(--brand-grey); }
  .standalone .name { font-size: 48px; }
  .standalone .descriptor { font-size: 17px; font-weight: 700; }

  /* Business cards */
  .card { position: absolute; left: 842px; width: 298px; }
  .card-front { top: 652px; height: 194px; background: var(--brand-blue); color: var(--paper); }
  .card-front .card-rule { position: absolute; left: 63px; top: 14px; width: 1px; height: 162px; background: rgba(255,255,255,0.55); }
  .card-front .wordmark { left: 38px; top: 72px; }
  .card-front .dot { width: 40px; height: 40px; background: var(--paper); }
  .card-front .name { font-size: 36px; }
  .card-front .descriptor-line {
    position: absolute; left: 74px; top: 166px; font-size: 14.5px; font-weight: 300;
    letter-spacing: 0.04em; color: rgba(255,255,255,0.85);
  }

  .card-back { top: 889px; height: 195px; background: var(--paper); border-bottom: 6px solid var(--brand-blue); }
  .card-back .holder { position: absolute; top: 53px; width: 100%; text-align: center; }
  .card-back .holder-name { font-size: 12px; font-weight: 700; color: var(--brand-blue); letter-spacing: 0.02em; }
  .card-back .holder-role { font-size: 8px; font-weight: 700; margin-top: 1px; }
  .card-back .details {
    position: absolute; top: 110px; font-size: 10px; line-height: 13.2px;
  }
  .card-back .details.phone { left: 22px; top: 112px; }
  .card-back .details.company { left: 193px; top: 98px; }
  .card-back .details strong { font-weight: 700; }
</style>
</head>
<body>

  <section class="letterhead" aria-label="Briefbogen">
    <div class="wordmark">
      <span class="dot"></span>
      <span>
        <span class="name">MARLOX</span>
        <span class="descriptor">PROJEKTMANAGEMENT</span>
      </span>
    </div>

    <div class="letter-rule"></div>

    <div class="letter-body">
      <p>Sehr geehrter Herr John Doe,</p>
      <p>Sed ut perspiciatis unde omnis iste natus error sit voluptatem accusantium doloremque laudantium, totam rem aperiam, eaque ipsa quae ab illo inventore veritatis et quasi architecto beatae vitae dicta sunt explicabo.</p>
      <p>Nemo enim ipsam voluptatem quia voluptas sit aspernatur aut odit aut fugit, sed quia consequuntur magni dolores eos qui ratione voluptatem sequi nesciunt. Neque porro quisquam est, qui dolorem ipsum quia dolor sit amet, consectetur, adipisci velit, sed quia non numquam eius modi tempora incidunt ut labore et dolore magnam aliquam quaerat voluptatem.</p>
      <p>Ut enim ad minima veniam, quis nostrum exercitationem ullam corporis suscipit laboriosam, nisi ut aliquid ex ea commodi consequatur? Quis autem vel eum iure reprehenderit qui in ea voluptate velit esse quam nihil molestiae consequatur, vel illum qui dolorem eum fugiat quo voluptas nulla pariatur?</p>
      <p class="closing">Mit freundlichen Grüßen</p>
      <p class="signature">Klaus Mustermann</p>
    </div>

    <svg class="contact-icon" width="34" height="28" viewBox="0 0 34 28" aria-hidden="true">
      <rect x="1" y="8" width="22" height="15" fill="#0b4c8e"/>
      <path d="M1 8 L12 17 L23 8" fill="none" stroke="#fff" stroke-width="1.6"/>
      <path d="M16 2 q2 -2 4 0 l1 3 q-2 2 0 5 q2 3 5 2 l3 1 q1 2 -1 4 q-4 2 -9 -3 q-5 -6 -3 -12z" fill="#0b4c8e" stroke="#fff" stroke-width="1"/>
      <path d="M27 20 h6 M30 17 v6" stroke="#0b4c8e" stroke-width="2.4"/>
    </svg>

    <address class="sender" style="font-style: normal;">
      <div class="group"><strong>MARLOX Projektmanagement</strong><br>Muster-Ring 13<br>12345 Musterstadt</div>
      <div class="group">Phone 01234 - 56789-0<br>Fax 01234 - 56789-1</div>
      <div class="group">info@mapm.de<br>www.ihredomain.de</div>
    </address>

    <div class="letter-band"></div>
  </section>

  <div class="wordmark standalone" aria-label="Marlox Projektmanagement">
    <span class="dot"></span>
    <span>
      <span class="name">MARLOX</span>
      <span class="descriptor">PROJEKTMANAGEMENT</span>
    </span>
  </div>

  <section class="card card-front" aria-label="Visitenkarte Vorderseite">
    <div class="card-rule"></div>
    <div class="wordmark">
      <span class="dot"></span>
      <span class="name">MARLOX</span>
    </div>
    <div class="descriptor-line">PROJEKTMANAGEMENT</div>
  </section>

  <section class="card card-back" aria-label="Visitenkarte Rückseite">
    <div class="holder">
      <div class="holder-name">KLAUS MUSTERMANN</div>
      <div class="holder-role">Creative Director</div>
    </div>
    <div class="details phone">
      Phone 01234 - 56789-0<br>Fax 01234 - 56789-1<br>Mail: info@mapm.de<br>Web: www.ihredomain.de
    </div>
    <div class="details company">
      <strong>MARLOX</strong><br>Projektmanagement<br>Muster-Ring 13<br>12345 Musterstadt<br>Deutschland
    </div>
  </section>

</body>
</html>
```